Business Card Design

Lawn service

Industry/Entity Type

Business

Contact Information for Business Card

Fern Hollow Lawn & Garden , deborah finch/owner,operater,2184 wexley millrd.. e. kellerton,tn. 30472, phone:912-555-0147, Residential,Commercial, Lawn and Landscape Maintenance, Bushhogging

```html
<!DOCTYPE html>
<html lang="en">
<head>
<meta charset="utf-8">
<title>Fern Hollow Lawn &amp; Garden — Business Card</title>
<link rel="stylesheet" href="https://fonts.googleapis.com/css2?family=Montserrat:wght@600;700&family=Quicksand:wght@400;500;600&display=swap">
<style>
  :root {
    --page-bg: #e9ebe8;
    --card-top: #ffffff;
    --card-top-shade: #e4e4e4;
    --green-dark: #0d9447;
    --green-light: #8cc63f;
    --logo-green: #109848;
    --text-light: #ffffff;
    --divider: rgba(255, 255, 255, 0.55);
  }
  * { box-sizing: border-box; margin: 0; padding: 0; }
  html, body {
    width: 1200px;
    height: 1000px;
    overflow: hidden;
    background: var(--page-bg);
  }
  .canvas {
    position: relative;
    width: 1200px;
    height: 1000px;
  }
  .business-card {
    position: absolute;
    left: 100px;
    top: 215px;
    width: 1000px;
    height: 570px;
    overflow: hidden;
    box-shadow: 0 10px 30px rgba(0, 0, 0, 0.18);
  }
  .card-header {
    position: absolute;
    inset: 0 0 auto 0;
    height: 330px;
    background: radial-gradient(ellipse at 45% 40%, var(--card-top) 0%, var(--card-top) 35%, var(--card-top-shade) 100%);
  }
  .brand {
    position: absolute;
    left: 0;
    right: 0;
    top: 92px;
    display: flex;
    align-items: center;
    justify-content: center;
    gap: 22px;
  }
  .brand-dot {
    width: 70px;
    height: 70px;
    border-radius: 50%;
    background: var(--logo-green);
    flex: none;
  }
  .brand-name {
    font-family: "Quicksand", sans-serif;
    font-weight: 600;
    font-size: 58px;
    line-height: 1.05;
    color: var(--logo-green);
    letter-spacing: 0.5px;
  }
  .service-band {
    position: absolute;
    left: 0;
    right: 0;
    top: 330px;
    height: 30px;
    background: var(--green-light);
    display: flex;
    align-items: center;
    justify-content: flex-end;
    padding-right: 36px;
  }
  .service-list {
    font-family: "Quicksand", sans-serif;
    font-weight: 500;
    font-size: 20px;
    color: var(--text-light);
    white-space: nowrap;
  }
  .card-footer {
    position: absolute;
    left: 0;
    right: 0;
    top: 360px;
    bottom: 0;
    background: var(--green-dark);
  }
  .person {
    position: absolute;
    left: 62px;
    top: 62px;
    color: var(--text-light);
    text-align: right;
  }
  .person-name {
    font-family: "Montserrat", sans-serif;
    font-weight: 700;
    font-size: 34px;
    text-transform: uppercase;
    letter-spacing: 0.5px;
    white-space: nowrap;
  }
  .person-title {
    font-family: "Montserrat", sans-serif;
    font-weight: 600;
    font-size: 27px;
    margin-top: 6px;
    margin-right: 8px;
    white-space: nowrap;
  }
  .divider {
    position: absolute;
    left: 520px;
    top: 28px;
    width: 1px;
    height: 128px;
    background: var(--divider);
  }
  .contact {
    position: absolute;
    left: 548px;
    top: 36px;
    list-style: none;
    color: var(--text-light);
    font-family: "Quicksand", sans-serif;
    font-weight: 500;
    font-size: 27px;
    line-height: 1.2;
    white-space: nowrap;
  }
  .contact-item {
    display: flex;
    align-items: flex-start;
    gap: 16px;
    margin-bottom: 8px;
  }
  .contact-icon {
    width: 32px;
    height: 32px;
    flex: none;
    margin-top: 1px;
  }
</style>
</head>
<body>
<main class="canvas">
  <article class="business-card">
    <header class="card-header">
      <div class="brand">
        <span class="brand-dot"></span>
        <h1 class="brand-name">Fern Hollow<br>Lawn &amp; Garden</h1>
      </div>
    </header>

    <div class="service-band">
      <p class="service-list">Residential,Commercial, Lawn and Landscape Maintenance, Bushhogging</p>
    </div>

    <section class="card-footer">
      <div class="person">
        <p class="person-name">Deborah Finch</p>
        <p class="person-title">owner,operater</p>
      </div>

      <span class="divider"></span>

      <ul class="contact">
        <li class="contact-item">
          <svg class="contact-icon" viewBox="0 0 32 32" aria-hidden="true">
            <circle cx="16" cy="16" r="15" fill="#ffffff"/>
            <rect x="11" y="7" width="10" height="18" rx="2" fill="none" stroke="#0d9447" stroke-width="2"/>
            <rect x="13" y="10" width="6" height="6" fill="#0d9447"/>
            <circle cx="16" cy="21.5" r="1.3" fill="#0d9447"/>
          </svg>
          <span>912-555-0147</span>
        </li>
        <li class="contact-item">
          <svg class="contact-icon" viewBox="0 0 32 32" aria-hidden="true">
            <circle cx="16" cy="16" r="15" fill="#ffffff"/>
            <path d="M16 7c-3.9 0-7 3-7 6.8 0 5 7 11.2 7 11.2s7-6.2 7-11.2C23 10 19.9 7 16 7z" fill="#0d9447"/>
            <circle cx="16" cy="13.8" r="2.6" fill="#ffffff"/>
          </svg>
          <span>2184 wexley mill rd<br>e. kellerton,tn. 30472</span>
        </li>
      </ul>
    </section>
  </article>
</main>
</body>
</html>
```